Long Term Contract - Wordpress Designers Wanted!

We are rapidly growing start-up web development company, focused on website development geared towards the insurance industry.

To increase our impact, we’ve decided to add a freelance designer to the team to assist in graphical elements and webdesign for our clients and template development.

This is to screen for a LONG TERM relationship where we will work together to design and develop sites for insurance agents. We are seeking a talented web designer with experience in WordPress and WordPress theme development to work his/her magic on our new websites.

To win this contest, please create an example website design for an individual insurance agent that sells auto and home insurance. The website will essentially be a "business card" for the agent and will generate trust, show experience, and most importantly create a call to action for the person to call or get a quote.

An example is here:

http://tallowgrid.com/heron/

As part of the deliverable, we will want you to integrate these templates as child themes under Quillix "Marlow" template framework - which we can provide you of course. All forms should be done in velvet forms.

Target Market(s)

Audience: consumers shopping for insurance agent

Industry/Entity Type

Insurance

Requirements
Must have
• Pages:
-home
-products
-about
-news/blog
-Contact us

On home page the following elements should be included:
-contact us form
-agent contact information
-blog entries
-testimonial
-agency overview
Should not have
• flash

```html
<!DOCTYPE html>
<html lang="en">
<head>
<meta charset="utf-8">
<title>Insurance Agent</title>
<link href="https://fonts.googleapis.com/css2?family=Ubuntu:wght@400;500;700&family=Kalam:wght@400;700&family=Arimo:wght@400;700&display=swap" rel="stylesheet">
<style>
:root{
  --red:#e8173a;
  --red-dark:#c50f2d;
  --ink:#1d1d1d;
  --grey:#6d6d6d;
  --paper:#efebe8;
  --card:#f7f5f3;
  --panel:#262626;
  --field:#3d3d3d;
  --footer:#2d2d2d;
  --sky:#dbe5ee;
  --house:#cdb48e;
  --lawn:#7da24a;
}
*{margin:0;padding:0;box-sizing:border-box}
html,body{width:920px;height:1200px;overflow:hidden}
body{background:var(--paper);font-family:"Arimo",Arial,sans-serif;color:var(--ink);position:relative}
.abs{position:absolute}
.logo{left:90px;top:30px;font-family:"Ubuntu",sans-serif;font-weight:700;font-size:34px;color:var(--red);letter-spacing:.5px}
.logo span{color:var(--ink)}
.callout{left:602px;top:33px;display:flex;gap:10px;align-items:center}
.callout .lines{font-family:"Kalam",cursive;text-align:right;line-height:1}
.callout .lead{font-size:19px;color:#333}
.callout .num{font-size:25px;font-weight:700;color:var(--red)}
.nav{left:78px;top:102px;width:766px;height:32px;background:linear-gradient(#f0304f,var(--red-dark));border-radius:3px;display:flex;padding-left:14px}
.nav a{color:#fff;text-decoration:none;font-size:12px;padding:0 17px;line-height:32px;border-right:1px solid rgba(0,0,0,.18)}
.nav a.active{background:#1f1f1f}
.hero{left:73px;top:150px;width:523px;height:271px;
  background:linear-gradient(180deg,var(--sky) 0%,#d9d2c4 22%,var(--house) 45%,#b89c76 62%,#93ad5c 74%,var(--lawn) 100%);
  box-shadow:0 2px 6px rgba(0,0,0,.15)}
.apply{left:603px;top:150px;width:245px;height:271px;background:var(--panel);border-radius:2px}
.apply .head{height:63px;background:linear-gradient(#444,#2a2a2a);display:flex;align-items:center;padding-left:22px;gap:8px;border-bottom:1px solid #111}
.apply .head h2{font-family:"Kalam",cursive;color:#fff;font-size:26px;font-weight:400}
.apply input{display:block;margin:0 0 8px 20px;width:198px;height:27px;border:1px solid #555;border-radius:4px;background:var(--field);color:#ddd;font-size:12px;padding-left:28px;font-family:"Arimo",sans-serif}
.apply input::placeholder{color:#ddd}
.apply form{padding-top:16px}
.apply button{margin:12px 0 0 27px;background:var(--red);border:0;color:#fff;font-family:"Kalam",cursive;font-size:18px;padding:3px 10px;height:30px}
.features{left:68px;top:450px;width:780px;display:flex;gap:14px}
.feature{width:192px}
.feature h3{display:flex;align-items:center;gap:8px;font-family:"Ubuntu",sans-serif;font-weight:500;font-size:17px;color:#7a7a7a;border-bottom:1px dotted #bbb;padding-bottom:4px;height:36px}
.feature p{font-size:9.5px;line-height:14.4px;color:var(--grey);letter-spacing:.6px;margin:16px 0 0 10px;text-align:justify}
.ico{width:30px;height:30px;border-radius:50%;flex:none}
.testi{left:74px;top:586px;width:772px;height:142px;background:var(--card);border-radius:10px}
.testi h2{position:absolute;left:15px;top:12px;font-family:"Ubuntu",sans-serif;font-size:18px;font-weight:700;color:var(--red)}
.testi h2 span{color:var(--ink)}
.viewall{position:absolute;right:36px;top:6px;background:var(--red);color:#fff;font-size:12px;padding:6px 16px}
.quotes{position:absolute;left:20px;top:38px;display:flex}
.quote{width:243px;padding:20px 20px 0 20px;border-right:1px dotted #bbb;height:96px;font-size:9.5px}
.quote:last-child{border:0}
.quote b.by{display:block;font-size:10px;margin-bottom:8px;letter-spacing:.5px}
.quote p{letter-spacing:.7px;line-height:14.5px;padding-left:6px;white-space:nowrap}
.quote .more{display:block;text-align:right;color:var(--red);font-weight:700;margin-top:10px;letter-spacing:.6px;font-size:10px}
.newshead{left:70px;top:745px;display:flex;align-items:center;gap:8px;font-family:"Ubuntu",sans-serif;font-weight:700;font-size:18px;color:var(--red)}
.newshead span{color:var(--ink)}
.post{left:70px;width:528px}
.date{position:absolute;left:0;top:4px;width:43px;height:50px;background:var(--red);color:#fff;text-align:center;border-radius:3px 3px 0 0;font-size:11px;line-height:12px;padding-top:4px}
.date b{display:block;font-size:15px;line-height:16px}
.post h3{margin-left:51px;font-family:"Ubuntu",sans-serif;font-weight:400;color:var(--red);font-size:14.5px}
.post .meta{margin-left:50px;font-size:9.5px;color:#999;margin-top:3px}
.post p{margin-left:50px;font-size:9.5px;line-height:14.4px;color:var(--grey);letter-spacing:.4px;margin-top:10px;text-align:justify}
.post .foot{margin-left:50px;margin-top:16px;display:flex;align-items:center;justify-content:space-between;font-size:10px;color:#555;padding-right:12px}
.share{display:flex;align-items:center;gap:4px}
.share i{width:14px;height:14px;background:#9a9a9a;border:1px solid #777;display:block}
.post .more{color:var(--red);margin-top:6px}
.rule{left:88px;top:950px;width:500px;border-top:1px dotted #ccc}
.contact{left:616px;top:755px;width:228px;height:360px;background:var(--card);padding:14px 12px}
.contact h2{display:flex;align-items:center;gap:8px;font-family:"Ubuntu",sans-serif;font-weight:700;font-size:18px;color:var(--red);margin-bottom:14px}
.contact h2 span{color:var(--ink)}
.contact p{font-size:9.5px;line-height:14.4px;letter-spacing:.8px;text-align:justify}
.contact h4{color:var(--red);font-weight:400;font-size:10.5px;margin:14px 0 6px}
.footer{left:0;top:1141px;width:920px;height:59px;background:var(--footer);color:#fff}
.footer .links{position:absolute;left:80px;top:12px;font-size:11.5px;word-spacing:2px}
.footer .links i{font-style:normal;margin:0 12px}
.footer .copy{position:absolute;left:80px;top:37px;font-size:11.5px}
.follow{position:absolute;left:632px;top:19px;display:flex;align-items:center;gap:10px;font-size:11.5px}
.follow i{width:18px;height:18px;border-radius:50%;background:#7b9fc4;display:block}
</style>
</head>
<body>
<div class="abs logo">Insurance <span>Agent</span></div>
<div class="abs callout">
  <svg width="42" height="40" viewBox="0 0 42 40" aria-hidden="true"><rect x="3" y="2" width="36" height="28" rx="6" fill="#5b5b5b"/><path d="M12 30 L10 38 L20 30Z" fill="#5b5b5b"/><circle cx="14" cy="16" r="3" fill="#ddd"/><circle cx="28" cy="16" r="3" fill="#ddd"/></svg>
  <div class="lines"><div class="lead">Call Now to find out how:</div><div class="num">+23 904 118 552</div></div>
</div>
<nav class="abs nav"><a class="active">Home</a><a>Products</a><a>About Us</a><a>News</a><a>Blog</a><a>Contact us</a></nav>

<div class="abs hero" role="img" aria-label="Photo of a family of four standing on the lawn in front of their brick house, with a red convertible car parked in the foreground"></div>
<aside class="abs apply">
  <div class="head">
    <svg width="30" height="30" viewBox="0 0 30 30" aria-hidden="true"><circle cx="15" cy="15" r="13" fill="#f08a1c" stroke="#fff" stroke-width="2"/><path d="M15 8v11M10 15l5 5 5-5" stroke="#fff" stroke-width="3" fill="none"/></svg>
    <h2>Apply Now</h2>
  </div>
  <form>
    <input placeholder="First Name"><input placeholder="Last Name"><input placeholder="Email"><input placeholder="Phone">
    <button type="button">Apply Now</button>
  </form>
</aside>

<section class="abs features">
  <div class="feature"><h3><svg class="ico" viewBox="0 0 30 30" aria-hidden="true"><circle cx="15" cy="15" r="13" fill="#fff" stroke="#e8173a" stroke-width="3"/><path d="M15 8v14M8 15h14" stroke="#e8173a" stroke-width="4"/></svg>Long Term Care</h3><p>Long Term Care Insurance covers you if you are unable to care for one's self due to an illness, injury or dis-ability for an extended</p></div>
  <div class="feature"><h3><span class="ico" role="img" aria-label="Syringe illustration" style="background:linear-gradient(135deg,#e33,#ccc)"></span>Medicare Plans</h3><p>Let us help you with your Medicare plan enrollment. Whether it be for hospital coverage or prescription benefits,we can help</p></div>
  <div class="feature"><h3><span class="ico" role="img" aria-label="First aid kit illustration" style="border-radius:4px;background:linear-gradient(#f4f4f8,#c9cde0)"></span>Life and Health</h3><p>Long Term Care Insurance covers you if you are unable to care for one's self due to an illness, injury or dis-ability for an extended</p></div>
  <div class="feature"><h3><span class="ico" role="img" aria-label="Rising sun illustration" style="background:radial-gradient(#ffd200,#f39a00)"></span>Fixed Annuities</h3><p>Long Term Care Insurance covers you if you are unable to care for one's self due to an illness, injury or dis-ability for an extended</p></div>
</section>

<section class="abs testi">
  <h2>What Other are <span>Saying About Us ?</span></h2>
  <span class="viewall">View all</span>
  <div class="quotes">
    <div class="quote"><b class="by">By Delphine</b><p>“it was fantastic to be able to win a<br><b>$50.00</b> won anything so this was great ”</p><span class="more">Readmore</span></div>
    <div class="quote"><b class="by">By Delphine</b><p>“it was fantastic to be able to win a<br><b>$50.00</b> won anything so this was great ”</p><span class="more">Readmore</span></div>
    <div class="quote"><b class="by">By Delphine</b><p>“it was fantastic to be able to win a<br><b>$50.00</b> won anything so this was great ”</p><span class="more">Readmore</span></div>
  </div>
</section>

<div class="abs newshead"><span class="ico" role="img" aria-label="News feed illustration" style="width:40px;height:36px;border-radius:4px;background:linear-gradient(#ffb347,#f07c00)"></span>Latest news and articles <span>from Insurance Agents</span></div>

<article class="abs post" style="top:800px">
  <div class="date">04<b>Mar</b>2012</div>
  <h3>Health care landscape shifting</h3>
  <div class="meta">Posted on March 4, 2012 by admin</div>
  <p>Lorem Ipsum is simply dummy text of the printing and typesetting industry. Lorem Ipsum has been the industry's standard dummy text ever since the 1500s, when an unknown printer took a galley of type and scrambled it to make a type specimen book. It has survived not only five centuries, but also the leap into electronic typesetting,</p>
  <div class="foot"><span class="share">Share This <i></i><i></i><i></i><i></i></span><span class="more">More info <b>[+]</b></span></div>
</article>
<div class="abs rule"></div>
<article class="abs post" style="top:970px">
  <div class="date">04<b>Mar</b>2012</div>
  <h3>Annuities offer safe haven in bad times</h3>
  <div class="meta">Posted on March 4, 2012 by admin</div>
  <p>Lorem Ipsum is simply dummy text of the printing and typesetting industry. Lorem Ipsum has been the industry's standard dummy text ever since the 1500s, when an unknown printer took a galley of type and scrambled it to make a type specimen book. It has survived not only five centuries, but also the leap into electronic typesetting,</p>
  <div class="foot"><span class="share">Share This <i></i><i></i><i></i><i></i></span><span class="more">More info <b>[+]</b></span></div>
</article>

<aside class="abs contact">
  <h2><span class="ico" role="img" aria-label="Contact card illustration" style="width:38px;height:36px;border-radius:3px;background:linear-gradient(#e6eef8,#9fb8d8)"></span>Contact <span>Us</span></h2>
  <p><b>We are located just across the Massachusetts border</b> in New Hampshire. We can serve your insurance needs in New Hampshire, Massachusetts, and Maine. You can contact us at:</p>
  <h4>Phone</h4>
  <p>Office: 1-877-402-7713 or 603-555-0148<br>Cell: 603-555-0192<br>Fax: 603-555-0167</p>
  <h4>Mail</h4>
  <p>42 Larkspur Ln.,<br>Fernbrook, NH 03099</p>
  <h4>Email</h4>
  <p>mara@heronbenefits.com</p>
</aside>

<footer class="abs footer">
  <div class="links">Home<i>|</i>Products<i>|</i>About Us<i>|</i>News<i>|</i>Blog<i>|</i>Contact us</div>
  <div class="copy">Copyright © Insurance Agents. All rights reserved.</div>
  <div class="follow">Follow us on : <i style="background:#f39a1c"></i><i></i><i style="background:#4a6fb5"></i><i style="background:#38a8e0"></i></div>
</footer>
</body>
</html>
```